Clean professional design needed for landscape property business

We need a logo for a new lawncare, landscaping , property maintenance business called Fernway Grove.
Our services include lawn mowing, garden maintenance, clean ups and some property maintenance.
We want a double sided business card that is clean and very professional using the colour scheme from our logo which is provided.
the business card should have impact as we will use these to drop into people's letterboxes as a marketing drop.
Initially we want to see what you come up with so there is a very wide scope here to work with.

Project Deadline Extended
Reason: we feel our original deadline was too short. we have extended to give more time for quality submissions.

Target Market(s)

High end property owners who don't wish to do there own gardneing or property maintenance

Industry/Entity Type

Business

Contact Information for Business Card

Name
Postion/ Title
Phone number
mobile
web address
physical address

services offered

Font styles to use
Sans Serif

Requirements
Must have
• curved edges preferrred
Nice to have
• We like the idea of the logo being embossed or etched into the card so it looks like it is below the surface of the card
Should not have
• No stock images or characters.

```html
<!DOCTYPE html>
<html lang="en">
<head>
<meta charset="utf-8">
<title>Fernway Grove — Business Card</title>
<link href="https://fonts.googleapis.com/css2?family=Arimo:wght@400;700&display=swap" rel="stylesheet">
<style>
  :root {
    --stage: #2e2e2f;
    --card-dark: #5a5a5c;
    --card-light: #ffffff;
    --green: #7cc21f;
    --ink: #4a4a4a;
    --ink-soft: #6b6b6b;
    --on-dark: #f1f1f1;
  }
  * { box-sizing: border-box; margin: 0; padding: 0; }
  html, body {
    width: 1200px; height: 900px; overflow: hidden;
    background: var(--stage);
    font-family: "Arimo", Arial, sans-serif;
  }
  .canvas { position: relative; width: 1200px; height: 900px; }
  .card {
    position: absolute; left: 320px; width: 560px; height: 320px;
    border-radius: 22px; overflow: hidden;
    box-shadow: 0 14px 30px rgba(0,0,0,.45);
  }
  .card--front { top: 95px; background: var(--card-dark); }
  .card--back { top: 475px; background: var(--card-light); }

  .wordmark {
    position: absolute; display: flex; align-items: center; gap: 12px;
    font-weight: 700; color: var(--green); letter-spacing: -0.5px; white-space: nowrap;
  }
  .wordmark__square { width: 16px; height: 16px; background: var(--green); }
  .card--front .wordmark { left: 60px; top: 90px; font-size: 52px; }
  .card--front .wordmark__square { width: 22px; height: 22px; }

  .services { position: absolute; left: 36px; top: 205px; list-style: none; }
  .services li {
    display: flex; align-items: center; gap: 14px;
    color: var(--on-dark); font-size: 15px; text-transform: uppercase;
    letter-spacing: .3px; margin-bottom: 10px;
  }
  .services li::before { content: ""; width: 18px; height: 12px; background: var(--green); }

  .card--back .wordmark { right: 36px; top: 34px; font-size: 30px; }
  .person { position: absolute; right: 36px; top: 110px; text-align: right; }
  .person__name { color: var(--green); font-size: 24px; }
  .person__title { color: var(--ink-soft); font-size: 14px; margin-top: 3px; }
  .address { position: absolute; right: 36px; top: 190px; text-align: right; color: var(--ink); font-size: 14px; line-height: 1.4; }

  .frame-line { position: absolute; inset: 0; }

  .contacts { position: absolute; left: 52px; top: 232px; list-style: none; }
  .contacts li { display: flex; align-items: center; gap: 10px; color: var(--ink); font-size: 15px; margin-bottom: 6px; }
  .contacts svg { width: 13px; height: 13px; fill: var(--green); }
</style>
</head>
<body>
<main class="canvas">
  <section class="card card--front" aria-label="Card front">
    <div class="wordmark"><span>fernway grove</span><span class="wordmark__square"></span></div>
    <ul class="services">
      <li>Lawn mowing</li>
      <li>Garden maintenance</li>
      <li>Clean ups &amp; some property maintenance</li>
    </ul>
  </section>

  <section class="card card--back" aria-label="Card back">
    <svg class="frame-line" width="560" height="320" viewBox="0 0 560 320" aria-hidden="true">
      <path d="M28 0 V205 H380" fill="none" stroke="var(--green)" stroke-width="3"/>
      <path d="M28 300 V320" fill="none" stroke="var(--green)" stroke-width="3"/>
    </svg>
    <div class="wordmark"><span>fernway grove</span><span class="wordmark__square"></span></div>
    <div class="person">
      <p class="person__name">Jordan Hale</p>
      <p class="person__title">Chief Executive Officer</p>
    </div>
    <p class="address">214 Linden Park Road<br>Suite 8, VA 20145</p>
    <ul class="contacts">
      <li><svg viewBox="0 0 16 16"><path d="M3 1h3l1.5 4-2 1.2a9 9 0 0 0 4.3 4.3L11 8.5l4 1.5v3a2 2 0 0 1-2 2A13 13 0 0 1 1 3a2 2 0 0 1 2-2z"/></svg>555-014-2261</li>
      <li><svg viewBox="0 0 16 16"><path d="M4 0h8a1 1 0 0 1 1 1v14a1 1 0 0 1-1 1H4a1 1 0 0 1-1-1V1a1 1 0 0 1 1-1zm1 2v10h6V2z"/></svg>555-018-9034</li>
      <li><svg viewBox="0 0 16 16"><circle cx="8" cy="8" r="7" fill="none" stroke="var(--green)" stroke-width="1.6"/><path d="M1 8h14M8 1c3 3 3 11 0 14M8 1c-3 3-3 11 0 14" fill="none" stroke="var(--green)" stroke-width="1.3"/></svg>www.fernwaygrove.com</li>
    </ul>
  </section>
</main>
</body>
</html>
```